Business Broker Website

This website will be for a business broker. The logo is attached and will need to be in the footer as it is but in the header please remove the word 'group' and replace with 'business sales' (so that it is marvello business sales).
It needs to be a modern high end corporate font for the logo and also for the rest of the site. Please only use fonts available on fonts.google.com
It needs to have 4 prominent boxes at the top of the page that say 'business listings', 'appraisal report', 'what we do' and 'who we are'
The 'what we do' section needs to have sub menu items for 'sectors' and 'services'. The who we are section needs to have sub menu items for 'about us' and 'team'
The top menu needs to have :
* Home
* Businesses for Sale
* Sell your Business
* What we do
* About Us
* Contact
This needs to be seen as the #1 business broker in Australia. It needs to attract serious high quality buyers and sellers and needs to be highly professional, premium and straight to the point and innovative.
It needs to show that Marvello Business Sales not only do SME sales but also do Corporate Mergers and Acquisitions.
They like the look of the site at https://brackwoodallies.example/en-us/
They also love the look of https://quorvenadvisers.example/ (they prefer this to the above site)
The website features a clean, minimalist layout with ample white space, making it easy to navigate and visually appealing. The typography is modern and legible, and the color palette is professional, enhancing the site's overall aesthetic. High-quality images and a responsive design contribute to its polished appearance.
Please note this is for an Australian based business.
Contact details to show in the footer:
Head Office
Suite 17, First Floor
48 Tamsin Street
Corrigan Flats
VIC 3412
1300 55 01 29
info@marvellogroup.example.au
If you need some wording for the site, look at https://www.marvellogroup.example.au/businesssales which is a page about their business division. Don't use all this content though as they want it straight to the point and not rambling on.

```html
<!DOCTYPE html>
<html lang="en">
<head>
<meta charset="utf-8">
<title>Marvello Business Sales</title>
<link href="https://fonts.googleapis.com/css2?family=Outfit:wght@400;500;600;700&family=Montserrat:wght@400;500;600&display=swap" rel="stylesheet">
<style>
:root{
  --orange:#ef4b24;
  --slate:#213744;
  --forest:#2e4a47;
  --ink:#1c1c1c;
  --muted:#555;
  --line:#d9d9d9;
  --black:#000;
  --white:#fff;
}
*{margin:0;padding:0;box-sizing:border-box}
html,body{width:1200px;height:3412px;overflow:hidden}
body{position:relative;font-family:"Montserrat",sans-serif;color:var(--ink);background:var(--white)}
.abs{position:absolute}
h1,h2,h3,.brand,.nav a,.btn,.card-label,.list li,.foot-head{font-family:"Outfit",sans-serif}

/* header + hero */
.hero{left:0;top:0;width:1200px;height:650px;background:linear-gradient(160deg,#3a4650 0%,#1d262e 45%,#2a2a2c 100%)}
.brand{left:99px;top:30px;display:flex;align-items:center;gap:12px;color:var(--white);font-weight:600;font-size:26px}
.brand i{display:block;width:30px;height:30px;border-radius:50%;background:var(--orange)}
.nav{left:483px;top:44px;display:flex;gap:0}
.nav a{color:var(--white);font-size:14px;font-weight:500;text-decoration:none;margin-right:30px}
.nav a.active{color:var(--orange)}
.hero-title{left:0;top:236px;width:1200px;text-align:center;color:var(--white);font-size:40px;font-weight:600;line-height:52px}
.btn{display:inline-flex;align-items:center;gap:8px;background:var(--orange);color:var(--white);font-size:16px;font-weight:600;height:46px;padding:0 22px;text-decoration:none}
.btn svg{width:15px;height:15px}
.btn.round{border-radius:0 23px 23px 0}
.hero-btn{left:502px;top:362px;border-radius:0 23px 23px 23px}
.chev{left:588px;top:564px}

/* feature boxes */
.box{top:650px;width:294px;height:301px;background:var(--slate);color:var(--white);text-align:center}
.box.hot{background:var(--orange)}
.box .ic{width:98px;height:98px;border-radius:50%;margin:45px auto 0;background:var(--orange);border:3px solid rgba(0,0,0,.25);display:flex;align-items:center;justify-content:center}
.box.hot .ic{background:var(--slate)}
.box h3{font-size:26px;font-weight:500;margin-top:30px}
.box p{font-size:13px;line-height:20px;margin:14px 30px 0}

/* who we are */
.sec-title{font-size:40px;font-weight:600;color:var(--ink)}
.kicker{font-size:16px;display:flex;align-items:center;gap:10px}
.kicker:after{content:"";width:28px;height:2px;background:var(--orange)}
.who-title{left:99px;top:1034px}
.who-kick{left:98px;top:1085px;color:var(--orange)}
.who-btn{left:97px;top:1146px}
.who-intro{left:528px;top:1036px;width:570px;font-size:16px;line-height:24px;color:var(--muted)}
.list{left:528px;top:1104px;list-style:none}
.list li{display:flex;align-items:center;gap:22px;font-size:16px;font-weight:500;height:33px;color:#222}
.list li svg{width:16px;height:16px}

/* what we do */
.wwd{left:0;top:1336px;width:1200px;height:599px;border-radius:106px 106px 0 0;background:linear-gradient(135deg,#3d5650 0%,#2b4543 50%,#35504c 100%)}
.wwd-title{left:99px;top:1380px;color:var(--white)}
.wwd-kick{left:99px;top:1432px;color:var(--white)}
.wwd-btn{left:97px;top:1491px}
.wwd-text{left:528px;top:1383px;width:600px;color:var(--white);font-size:16px;line-height:24px;font-weight:500}
.wwd-text p+p{margin-top:24px}
.card{top:1596px;width:320px;height:261px;border-radius:18px;overflow:hidden}
.card-label{position:absolute;left:0;bottom:18px;width:100%;text-align:center;color:var(--white);font-size:23px;font-weight:600}
.c1{left:99px;background:linear-gradient(180deg,#5c8fd0 0%,#8a6a66 50%,#3a3a40 100%)}
.c2{left:440px;background:linear-gradient(180deg,#8a6a55 0%,#c9603e 55%,#ef4b24 100%)}
.c3{left:780px;background:linear-gradient(180deg,#7aa7d6 0%,#8fa184 50%,#4f5b4a 100%)}

/* contact */
.contact-title{left:0;top:2036px;width:1200px;text-align:center}
.center-kick{left:0;width:1200px;justify-content:center;color:#333}
.center-kick:before{content:"";width:28px;height:2px;background:var(--orange)}
.field{height:57px;border:2px solid #e4e4e4;border-radius:6px;display:flex;align-items:center;gap:14px;padding-left:22px;font-size:13px;color:#444}
.field svg{width:12px;height:12px;fill:#c8c8c8}
.msg{height:166px;align-items:flex-start;padding-top:22px}
.send{left:522px;top:2539px;border-radius:0 23px 23px 23px}

/* signup + footer */
.footer{left:0;top:2859px;width:1200px;height:553px;background:var(--black)}
.signup{left:163px;top:2682px;width:881px;height:246px;background:var(--white);box-shadow:0 0 18px rgba(0,0,0,.08);text-align:center}
.signup h2{font-size:38px;font-weight:600;margin-top:28px}
.signup .kicker{position:static;width:auto;margin-top:10px}
.email{left:109px;top:140px;width:601px;height:42px;border:1px solid #dcdcdc;border-radius:4px;font-size:12px;color:#888;display:flex;align-items:center;padding-left:14px}
.search{left:722px;top:140px;width:43px;height:42px;border-radius:6px;background:var(--orange);display:flex;align-items:center;justify-content:center}
.foot-brand{left:114px;top:3130px;display:flex;align-items:center;gap:16px;font-family:"Outfit",sans-serif;font-size:54px;font-weight:600;color:#4a5a6e}
.foot-brand i{width:54px;height:54px;border-radius:50%;background:#4a5a6e;display:block}
.foot-head{color:var(--white);font-size:19px;font-weight:600}
.foot-head:after{content:"";display:block;width:48px;height:4px;background:var(--orange);margin-top:12px}
.links{left:507px;top:3104px;list-style:none}
.links li{display:flex;align-items:center;gap:12px;height:29px;color:var(--white);font-size:16px}
.links svg{width:14px;height:14px}
.cinfo{left:740px;color:var(--white);font-size:16px;line-height:22px;display:flex;gap:16px}
.cinfo svg{width:14px;height:14px;margin-top:4px;fill:#ccc;flex:none}
.rule{left:110px;top:3319px;width:976px;height:1px;background:#6fb4a8}
.copy{left:0;top:3357px;width:1200px;text-align:center;color:var(--white);font-size:15px;font-family:"Outfit",sans-serif;font-weight:500}
</style>
</head>
<body>

<div class="abs hero" role="img" aria-label="Looking up at city office towers against the sky, darkened"></div>
<div class="abs brand"><i></i>Marvello Business Sales</div>
<nav class="abs nav">
  <a class="active" href="#">Home</a><a href="#">Businesses for Sale</a><a href="#">Sell Your Business</a><a href="#">What We Do</a><a href="#">About Us</a><a href="#">Contact</a>
</nav>
<h1 class="abs hero-title">Our Partner in Melbourne<br>Real Estate and Business Sales</h1>
<a class="abs btn hero-btn" href="#">Get Started <svg viewBox="0 0 16 16"><circle cx="8" cy="8" r="8" fill="#fff"/><path d="M6.5 4.5 10 8l-3.5 3.5" stroke="#ef4b24" stroke-width="2" fill="none"/></svg></a>
<svg class="abs chev" width="24" height="16" viewBox="0 0 24 16"><path d="M3 3l9 9 9-9" stroke="#fff" stroke-width="2.5" fill="none"/></svg>

<section>
  <div class="abs box" style="left:0">
    <div class="ic"><svg width="50" height="50" viewBox="0 0 50 50" fill="none" stroke="#fff" stroke-width="2"><rect x="12" y="8" width="24" height="32" rx="2"/><path d="M18 16h12M18 23h12M18 30h8"/></svg></div>
    <h3>Business Listings</h3>
    <p>Lorem ipsum dolor sit amet, consectetur adipiscing elit, sed do eiusmod tempor</p>
  </div>
  <div class="abs box hot" style="left:302px">
    <div class="ic"><svg width="50" height="50" viewBox="0 0 50 50" fill="none" stroke="#fff" stroke-width="2"><rect x="12" y="8" width="24" height="32" rx="2"/><path d="M17 17l2 2 4-4M26 17h6M17 27l2 2 4-4M26 27h6M34 34l8-8"/></svg></div>
    <h3>Appraisal Report</h3>
    <p>Lorem ipsum dolor sit amet, consectetur adipiscing elit, sed do eiusmod tempor</p>
  </div>
  <div class="abs box" style="left:604px">
    <div class="ic"><svg width="50" height="50" viewBox="0 0 50 50" fill="none" stroke="#fff" stroke-width="2"><circle cx="25" cy="22" r="7"/><circle cx="13" cy="18" r="5"/><circle cx="37" cy="18" r="5"/><path d="M14 40c0-7 5-10 11-10s11 3 11 10M4 32c0-5 4-7 9-7M46 32c0-5-4-7-9-7"/></svg></div>
    <h3>What We Do</h3>
    <p>Lorem ipsum dolor sit amet, consectetur adipiscing elit, sed do eiusmod tempor</p>
  </div>
  <div class="abs box" style="left:906px">
    <div class="ic"><svg width="50" height="50" viewBox="0 0 50 50" fill="none" stroke="#fff" stroke-width="2"><circle cx="25" cy="17" r="8"/><path d="M11 42c0-9 6-14 14-14s14 5 14 14"/></svg></div>
    <h3>Who We Are</h3>
    <p>Lorem ipsum dolor sit amet, consectetur adipiscing elit, sed do eiusmod tempor</p>
  </div>
</section>

<h2 class="abs sec-title who-title">Who We Are</h2>
<div class="abs kicker who-kick">About Us</div>
<a class="abs btn round who-btn" href="#">Learn More <svg viewBox="0 0 16 16"><circle cx="8" cy="8" r="8" fill="#fff"/><path d="M6.5 4.5 10 8l-3.5 3.5" stroke="#ef4b24" stroke-width="2" fill="none"/></svg></a>
<p class="abs who-intro">The Marvello Group of Companies is based in Melbourne, Australia, and specialises in three main areas of expertise:</p>
<ul class="abs list">
  <li><svg viewBox="0 0 16 16"><circle cx="8" cy="8" r="8" fill="#ef4b24"/><path d="M4.5 8.2l2.3 2.3 4.7-4.7" stroke="#fff" stroke-width="2" fill="none"/></svg>Commercial &amp; Industrial Real Estate - Sales, Leasing &amp; Management</li>
  <li><svg viewBox="0 0 16 16"><circle cx="8" cy="8" r="8" fill="#ef4b24"/><path d="M4.5 8.2l2.3 2.3 4.7-4.7" stroke="#fff" stroke-width="2" fill="none"/></svg>Business Sales</li>
  <li><svg viewBox="0 0 16 16"><circle cx="8" cy="8" r="8" fill="#ef4b24"/><path d="M4.5 8.2l2.3 2.3 4.7-4.7" stroke="#fff" stroke-width="2" fill="none"/></svg>Residential Real Estate - Sales, Leasing &amp; Management</li>
  <li><svg viewBox="0 0 16 16"><circle cx="8" cy="8" r="8" fill="#ef4b24"/><path d="M4.5 8.2l2.3 2.3 4.7-4.7" stroke="#fff" stroke-width="2" fill="none"/></svg>Advocacy</li>
  <li><svg viewBox="0 0 16 16"><circle cx="8" cy="8" r="8" fill="#ef4b24"/><path d="M4.5 8.2l2.3 2.3 4.7-4.7" stroke="#fff" stroke-width="2" fill="none"/></svg>Owners Corporation</li>
</ul>

<div class="abs wwd" role="img" aria-label="Green foliage background with a dark green overlay"></div>
<h2 class="abs sec-title wwd-title">What We Do</h2>
<div class="abs kicker wwd-kick">Our Services</div>
<a class="abs btn round wwd-btn" href="#">Learn More <svg viewBox="0 0 16 16"><circle cx="8" cy="8" r="8" fill="#fff"/><path d="M6.5 4.5 10 8l-3.5 3.5" stroke="#ef4b24" stroke-width="2" fill="none"/></svg></a>
<div class="abs wwd-text">
  <p>Our Team of property, business and sales professionals is here for you.</p>
  <p>Whether you are looking for a trusted partner to manage your commercial or industrial property, help you purchase your next family home or find a buyer for your business who is willing to pay the right price – you have come to the right location.</p>
</div>
<div class="abs card c1" role="img" aria-label="Commercial building with a red arrow above it"><span class="card-label">Commercial &amp; Industrial</span></div>
<div class="abs card c2" role="img" aria-label="Business people shaking hands, orange tint"><span class="card-label">Business Sales</span></div>
<div class="abs card c3" role="img" aria-label="Suburban family home with garden"><span class="card-label">Residential</span></div>

<h2 class="abs sec-title contact-title">Contact Us</h2>
<div class="abs kicker center-kick" style="top:2099px">Get In Touch</div>
<div class="abs field" style="left:127px;top:2167px;width:458px"><svg viewBox="0 0 12 12"><circle cx="6" cy="3.5" r="3"/><path d="M0 12c0-4 3-5 6-5s6 1 6 5z"/></svg>First Name</div>
<div class="abs field" style="left:611px;top:2167px;width:458px"><svg viewBox="0 0 12 12"><circle cx="6" cy="3.5" r="3"/><path d="M0 12c0-4 3-5 6-5s6 1 6 5z"/></svg>Last Name</div>
<div class="abs field" style="left:127px;top:2248px;width:458px"><svg viewBox="0 0 12 12"><path d="M0 2h12v8H0z"/></svg>Email Address</div>
<div class="abs field" style="left:611px;top:2248px;width:458px"><svg viewBox="0 0 12 12"><path d="M2 0l3 3-1.5 2a7 7 0 0 0 3.5 3.5L9 7l3 3-2 2C5 12 0 7 0 2z"/></svg>Phone Number</div>
<div class="abs field msg" style="left:127px;top:2329px;width:942px"><svg viewBox="0 0 12 12"><path d="M0 2h12v8H0z"/></svg>Message</div>
<a class="abs btn send" href="#">Send Now <svg viewBox="0 0 16 16"><circle cx="8" cy="8" r="8" fill="#fff"/><path d="M6.5 4.5 10 8l-3.5 3.5" stroke="#ef4b24" stroke-width="2" fill="none"/></svg></a>

<footer class="abs footer"></footer>
<div class="abs signup">
  <h2>Sign up for the latest</h2>
  <div class="kicker center-kick">News from Marvello Business Sales</div>
  <div class="abs email">Enter your email id</div>
  <div class="abs search"><svg width="18" height="18" viewBox="0 0 18 18" fill="none" stroke="#fff" stroke-width="2.5"><circle cx="7.5" cy="7.5" r="5.5"/><path d="M11.5 11.5l5 5"/></svg></div>
</div>

<div class="abs foot-brand"><i></i>Marvello Group</div>
<div class="abs foot-head" style="left:507px;top:3033px">QUICK LINKS</div>
<ul class="abs links">
  <li><svg viewBox="0 0 16 16"><circle cx="8" cy="8" r="8" fill="#ef4b24"/><path d="M6.5 4.5 10 8l-3.5 3.5" stroke="#000" stroke-width="2" fill="none"/></svg>Home</li>
  <li><svg viewBox="0 0 16 16"><circle cx="8" cy="8" r="8" fill="#ef4b24"/><path d="M6.5 4.5 10 8l-3.5 3.5" stroke="#000" stroke-width="2" fill="none"/></svg>Businesses for Sale</li>
  <li><svg viewBox="0 0 16 16"><circle cx="8" cy="8" r="8" fill="#ef4b24"/><path d="M6.5 4.5 10 8l-3.5 3.5" stroke="#000" stroke-width="2" fill="none"/></svg>Sell Your Business</li>
  <li><svg viewBox="0 0 16 16"><circle cx="8" cy="8" r="8" fill="#ef4b24"/><path d="M6.5 4.5 10 8l-3.5 3.5" stroke="#000" stroke-width="2" fill="none"/></svg>What We Do</li>
  <li><svg viewBox="0 0 16 16"><circle cx="8" cy="8" r="8" fill="#ef4b24"/><path d="M6.5 4.5 10 8l-3.5 3.5" stroke="#000" stroke-width="2" fill="none"/></svg>About Us</li>
  <li><svg viewBox="0 0 16 16"><circle cx="8" cy="8" r="8" fill="#ef4b24"/><path d="M6.5 4.5 10 8l-3.5 3.5" stroke="#000" stroke-width="2" fill="none"/></svg>Contact</li>
</ul>
<div class="abs foot-head" style="left:740px;top:3033px">CONTACT US</div>
<div class="abs cinfo" style="top:3104px"><svg viewBox="0 0 14 14"><path d="M7 0a5 5 0 0 1 5 5c0 4-5 9-5 9S2 9 2 5a5 5 0 0 1 5-5zm0 3a2 2 0 1 0 0 4 2 2 0 0 0 0-4z"/></svg><span>Suite 17, First Floor 48 Tamsin Street<br>Corrigan Flats VIC 3412</span></div>
<div class="abs cinfo" style="top:3169px"><svg viewBox="0 0 14 14"><path d="M2 0l3 3-1.5 2.5a8 8 0 0 0 5 5L11 9l3 3-2 2C6 14 0 8 0 2z"/></svg><span>1300 55 01 29</span></div>
<div class="abs cinfo" style="top:3220px"><svg viewBox="0 0 14 14"><path d="M0 2h14v1L7 8 0 3zM0 5l7 5 7-5v7H0z"/></svg><span>info@marvellogroup.example.au</span></div>
<div class="abs rule"></div>
<div class="abs copy">Copyright &nbsp;2025 Marvello Business Sales. All rights reserved</div>

</body>
</html>
```